New Branding Business Card Design

Redesign business card according to new branding update.

** The design received so far are single color + BLACK.
I'd encourage designer to use different tones of blue / purple as described in the Designer Brief color palette

Target Market(s)

International

Industry/Entity Type

Medical Equipment

Contact Information for Business Card

Logo on one side (Designer can decide if they want to move certain info from the other side to save space)

Main body info (company name, individual name in both English and Chinese, contact info etc) on the other
Prefer a 'cleaner' layout - vs 'all over the place'
Prefer flush left alignment

Font styles to use
Sans Serif

Requirements
Must have
• Key info
• (Company name (English)): VORAK (HK) Limited
• (Name (English)): Martin L. Osei
• (Credential): FCPA, FHKSI
• (Title): Founder, Managing Director & CEO
• For the following info, designers decide whether to use colon or no colon, stroke separator, or use icon gfx for T (for telephone fixed line, M for mobile etc.)
• T: +852 2741 VORAK / +852 2741 5317
• M: +852 9473 6215 / + 86 139 4527 3916
• E: martin.l.osei@vorak-example.hk
Nice to have
• Depending on the space and spacing available designers can add or use fuller title and other info
• Title: Chairman of the Executive Committee, Founder, Managing Director & CEO
• (Name (Chinese)): 梁文浩
Should not have
• One of our business entities a long company name that cannot be broken into 2 lines
• makes vertical implementation almost impossible

```html
<!DOCTYPE html>
<html lang="en">
<head>
<meta charset="utf-8">
<title>VORAK (HK) Limited – Business Card</title>
<link rel="stylesheet" href="https://fonts.googleapis.com/css2?family=Open+Sans:wght@400;700&family=Oswald:wght@400&family=Noto+Sans+TC:wght@500&display=swap">
<style>
  :root {
    --stage: #2d2d2d;
    --brand-purple: #5a2d82;
    --paper: #ffffff;
    --ink-grey: #4a4a4a;
    --rule-grey: #d9d9d9;
  }
  * { box-sizing: border-box; margin: 0; padding: 0; }
  html, body { width: 1200px; height: 866px; overflow: hidden; }
  body {
    background: var(--stage);
    display: flex;
    align-items: center;
    justify-content: center;
    gap: 40px;
    font-family: "Open Sans", Arial, sans-serif;
  }
  .card {
    width: 520px;
    height: 300px;
    position: relative;
    box-shadow: 0 10px 24px rgba(0,0,0,0.45);
    overflow: hidden;
  }

  /* Front */
  .card-front {
    background: var(--paper);
    border-bottom: 7px solid var(--brand-purple);
    display: flex;
    align-items: center;
  }
  .brand-block {
    width: 190px;
    display: flex;
    align-items: center;
    justify-content: center;
    gap: 10px;
  }
  .brand-square {
    width: 22px;
    height: 22px;
    border-radius: 4px;
    background: var(--brand-purple);
  }
  .brand-name {
    font-weight: 700;
    font-size: 30px;
    letter-spacing: 2px;
    color: var(--brand-purple);
  }
  .divider {
    width: 1px;
    height: 190px;
    background: var(--rule-grey);
  }
  .details {
    padding-left: 24px;
    padding-right: 20px;
  }
  .person-name {
    font-weight: 700;
    font-size: 14.5px;
    text-transform: uppercase;
    color: var(--brand-purple);
    letter-spacing: 0.3px;
  }
  .person-name .credentials { font-size: 12px; margin-left: 3px; }
  .person-name-zh {
    font-family: "Noto Sans TC", "Open Sans", sans-serif;
    font-weight: 500;
    font-size: 22px;
    line-height: 1.2;
    color: var(--brand-purple);
    margin-top: 1px;
  }
  .job-title {
    font-size: 13px;
    color: var(--ink-grey);
    line-height: 1.35;
    margin-top: 2px;
  }
  .contact-list {
    list-style: none;
    margin-top: 12px;
    font-size: 12.5px;
    color: var(--ink-grey);
    line-height: 1.5;
  }
  .contact-list li { display: flex; align-items: center; gap: 8px; }
  .contact-list svg { width: 12px; height: 12px; flex: none; fill: var(--brand-purple); }

  /* Back */
  .card-back {
    background: var(--brand-purple);
    display: flex;
    align-items: center;
    justify-content: center;
  }
  .entity-name {
    font-family: "Oswald", "Arial Narrow", sans-serif;
    font-weight: 400;
    font-size: 27px;
    color: var(--paper);
    text-transform: uppercase;
    letter-spacing: 0.2px;
  }
</style>
</head>
<body>
  <svg width="0" height="0" style="position:absolute">
    <defs>
      <symbol id="icon-phone" viewBox="0 0 12 12"><path d="M1 4.5C1 3 2.5 2 6 2s5 1 5 2.5V5H8.5V4C7.8 3.8 4.2 3.8 3.5 4v1H1z"/><path d="M3 6h6l1.5 4.5h-9z"/></symbol>
      <symbol id="icon-mobile" viewBox="0 0 12 12"><path d="M2 1.5h8v9H2zM3.3 2.8v6.4h5.4V2.8z" fill-rule="evenodd"/></symbol>
      <symbol id="icon-mail" viewBox="0 0 12 12"><path d="M0.5 2.5h11v7h-11z"/><path d="M0.5 2.5L6 7l5.5-4.5" fill="none" stroke="#fff" stroke-width="1"/></symbol>
    </defs>
  </svg>

  <section class="card card-front">
    <div class="brand-block">
      <span class="brand-square"></span>
      <span class="brand-name">VORAK</span>
    </div>
    <div class="divider"></div>
    <div class="details">
      <p class="person-name">Martin L. Osei <span class="credentials">FCPA, FHKSI</span></p>
      <p class="person-name-zh">梁文浩</p>
      <p class="job-title">Founder<br>Managing Director &amp; CEO</p>
      <ul class="contact-list">
        <li><svg><use href="#icon-phone"/></svg>+852 2741 VORAK</li>
        <li><svg><use href="#icon-phone"/></svg>+852 2741 5317</li>
        <li><svg><use href="#icon-mobile"/></svg>+852 9473 6215</li>
        <li><svg><use href="#icon-mobile"/></svg>+ 86 139 4527 3916</li>
        <li><svg><use href="#icon-mail"/></svg>martin.l.osei@vorak-example.hk</li>
      </ul>
    </div>
  </section>

  <section class="card card-back">
    <p class="entity-name">Halvern Bio-Medical Limited</p>
  </section>
</body>
</html>
```